Zest Glide : Stubborn Bug Remover

We are looking at bringing a "Zest-glide" formula to market that you mist and wipe onto your paint to remove stubborn bug guts and smudges from bug build up

```html
<!DOCTYPE html>
<html lang="en">
<head>
<meta charset="utf-8">
<title>Zest Glide – Bug Remover Label</title>
<link href="https://fonts.googleapis.com/css2?family=Bebas+Neue&family=Lato:wght@400;700&family=Montserrat:wght@800&display=swap" rel="stylesheet">
<style>
  :root {
    --backdrop: #c9ccd1;
    --label-black: #0b0b0b;
    --label-charcoal: #1c1c1c;
    --amber: #f2a812;
    --amber-glow-strong: rgba(242,168,18,0.55);
    --amber-glow-soft: rgba(242,168,18,0.2);
    --amber-glow-none: rgba(242,168,18,0);
    --white: #ffffff;
  }
  html, body {
    margin: 0;
    padding: 0;
    width: 948px;
    height: 1200px;
    overflow: hidden;
    background: var(--backdrop);
  }
  .canvas {
    position: relative;
    width: 948px;
    height: 1200px;
  }
  .label {
    position: absolute;
    left: 174px;
    top: 32px;
    width: 600px;
    height: 1136px;
    background: radial-gradient(ellipse at 55% 45%, var(--label-charcoal) 0%, var(--label-black) 70%);
    overflow: hidden;
    font-family: "Lato", sans-serif;
    color: var(--white);
  }
  .band {
    position: absolute;
    left: 0;
    width: 100%;
    background: var(--amber);
  }
  .band--top-wide { top: 0; height: 33px; }
  .band--top-thin { top: 38px; height: 6px; }
  .band--bottom-thin { bottom: 38px; height: 6px; }
  .band--bottom-wide { bottom: 0; height: 33px; }

  .tagline-row {
    position: absolute;
    left: 0;
    width: 100%;
    height: 16px;
    display: flex;
    justify-content: center;
    align-items: center;
    gap: 12px;
    font-size: 11px;
    font-weight: 400;
    line-height: 16px;
    white-space: nowrap;
  }
  .tagline-row--top { top: 57px; }
  .tagline-row--bottom { top: 1068px; }
  .tagline-row .dot {
    flex: 0 0 auto;
    display: block;
    width: 5px;
    height: 5px;
    border-radius: 50%;
    background: var(--white);
  }

  .hero-illustration {
    position: absolute;
    left: 140px;
    top: 140px;
    width: 390px;
    height: 340px;
    background: radial-gradient(closest-side, var(--amber-glow-strong) 0%, var(--amber-glow-soft) 50%, var(--amber-glow-none) 100%);
  }

  .product-name {
    position: absolute;
    margin: 0;
    left: 0;
    top: 520px;
    width: 100%;
    text-align: center;
    font-family: "Bebas Neue", sans-serif;
    font-weight: 400;
    font-size: 150px;
    line-height: 1;
    letter-spacing: 4px;
    color: var(--white);
  }

  .feature-badges {
    position: absolute;
    top: 818px;
    left: 0;
    width: 100%;
    display: flex;
    justify-content: center;
    gap: 46px;
  }
  .badge {
    width: 64px;
    height: 64px;
    border: 2px solid var(--amber);
    border-radius: 50%;
    box-sizing: border-box;
    display: flex;
    flex-direction: column;
    align-items: center;
    justify-content: center;
  }
  .badge__number {
    font-family: "Bebas Neue", sans-serif;
    font-size: 30px;
    line-height: 0.85;
    color: var(--amber);
  }
  .badge__caption {
    font-family: "Montserrat", sans-serif;
    font-weight: 800;
    font-size: 8px;
    line-height: 1;
    color: var(--white);
    margin-top: 2px;
  }
  .badge__caption--hours { font-size: 11px; margin-top: 0; }
  .badge svg { display: block; }

  .claim {
    position: absolute;
    margin: 0;
    left: 0;
    top: 978px;
    width: 100%;
    text-align: center;
    font-family: "Bebas Neue", sans-serif;
    font-size: 23px;
    line-height: 1.3;
    letter-spacing: 0.3px;
    color: var(--white);
  }
</style>
</head>
<body>
<div class="canvas">
  <section class="label" aria-label="Zest Glide spray can label">
    <div class="band band--top-wide"></div>
    <div class="band band--top-thin"></div>

    <div class="tagline-row tagline-row--top">
      <span>LOREM IPSUM DOLOR SIT AMET</span><span class="dot"></span>
      <span>LOREM IPSUM DOLOR SIT AMET</span><span class="dot"></span>
      <span>LOREM IPSUM DOLOR SIT AMET</span>
    </div>

    <div class="hero-illustration" role="img" aria-label="Brushed amber illustration of a fly wearing a gas mask"></div>

    <h1 class="product-name">Zest Glide</h1>

    <div class="feature-badges">
      <div class="badge">
        <span class="badge__number">24</span>
        <span class="badge__caption badge__caption--hours">HRS</span>
      </div>
      <div class="badge">
        <svg width="18" height="24" viewBox="0 0 18 24" aria-hidden="true">
          <path d="M9 1 C9 1 1 11 1 16 A8 8 0 0 0 17 16 C17 11 9 1 9 1 Z" fill="var(--amber)"/>
          <path d="M5 16 A4 4 0 0 0 11 19" stroke="var(--label-black)" stroke-width="1.6" fill="none"/>
        </svg>
        <span class="badge__caption">PROOF</span>
      </div>
      <div class="badge">
        <svg width="26" height="20" viewBox="0 0 26 20" aria-hidden="true">
          <path d="M3 6 L11 18 L15 8" stroke="var(--amber)" stroke-width="2.4" fill="none" stroke-linecap="round" stroke-linejoin="round"/>
          <path d="M14 10 C14 4 19 1 25 1 C25 7 21 11 14 10 Z" fill="var(--amber)"/>
        </svg>
        <span class="badge__caption">NATURAL</span>
      </div>
    </div>

    <p class="claim">LOREM IPSUM DOLOR<br>SIT AMET</p>

    <div class="tagline-row tagline-row--bottom">
      <span>LOREM IPSUM DOLOR SIT AMET</span><span class="dot"></span>
      <span>LOREM IPSUM DOLOR SIT AMET</span><span class="dot"></span>
      <span>LOREM IPSUM DOLOR SIT AMET</span>
    </div>

    <div class="band band--bottom-thin"></div>
    <div class="band band--bottom-wide"></div>
  </section>
</div>
</body>
</html>
```